Business card and e-mail signature template.

I need a business card- and e-mail signature template for a project (signature will be used with gmail). The logo is attached.

There the logo has a focus on the “Lumora” part of the name. The URL for the project is www.lumorafest.com.
The full name of the project is The Lumora Expo. The project will be publicly known as “Lumora” or “Lumora2020”. In all documents we will present the project as Lumora2020.

The logo can contain design elements and the design should be modern and appealing to both young people and traditional companies.

This competition is part of a bigger delivery. The winner will therefore be a strong candidate for the brand guide og maybe website.

```html
<!DOCTYPE html>
<html lang="en">
<head>
<meta charset="utf-8">
<title>Lumora2020 – E-mail Signature</title>
<link rel="stylesheet" href="https://fonts.googleapis.com/css2?family=Roboto:wght@400;500;700&display=swap">
<style>
  :root {
    --page-bg: #f3f3f3;
    --card-top: #ffffff;
    --card-bottom: #e9e9e9;
    --ink: #333333;
    --ink-soft: #444444;
    --pink: #e8265e;
    --teal: #1bb1b5;
    --orange: #f58220;
    --purple: #8b1e7a;
    --photo-light: #c9d3df;
    --photo-dark: #6f8fc7;
  }
  * { margin: 0; padding: 0; box-sizing: border-box; }
  html, body {
    width: 1200px; height: 1004px; overflow: hidden;
    background: var(--page-bg);
    font-family: "Roboto", Arial, sans-serif;
    color: var(--ink);
  }
  .signature {
    position: absolute;
    left: 76px; top: 347px;
    width: 1047px; height: 311px;
    background: linear-gradient(180deg, var(--card-top) 0%, var(--card-bottom) 100%);
  }
  .portrait-ring {
    position: absolute;
    left: 51px; top: 67px;
    width: 176px; height: 176px;
    border-radius: 50%;
    border: 3px solid var(--pink);
    background: #ffffff;
  }
  .portrait {
    position: absolute;
    left: 9px; top: 9px;
    width: 152px; height: 152px;
    border-radius: 50%;
    background: radial-gradient(circle at 50% 35%, var(--photo-light) 0%, #b9c4d4 45%, var(--photo-dark) 100%);
  }
  .divider {
    position: absolute;
    left: 260px; top: 40px;
    width: 2px; height: 231px;
    background: var(--pink);
  }
  .name {
    position: absolute;
    left: 295px; top: 34px;
    font-size: 37px; font-weight: 700;
    letter-spacing: 0.2px;
    color: var(--ink);
  }
  .role {
    position: absolute;
    left: 296px; top: 78px;
    font-size: 20px; font-weight: 400;
    color: var(--ink-soft);
  }
  .contacts {
    position: absolute;
    left: 303px; top: 134px;
    list-style: none;
  }
  .contacts li {
    display: flex; align-items: center;
    height: 27px;
    font-size: 20px;
    color: var(--ink);
  }
  .contacts svg { width: 17px; height: 17px; margin-right: 12px; flex: none; }
  .contacts .accent { color: var(--pink); }
  .socials {
    position: absolute;
    left: 296px; top: 248px;
    display: flex; gap: 11px;
  }
  .socials span {
    display: block; width: 24px; height: 24px; border-radius: 3px;
  }
  .socials .s1 { background: var(--pink); }
  .socials .s2 { background: var(--teal); }
  .socials .s3 { background: var(--orange); }
  .socials .s4 { background: var(--purple); }
  .brand {
    position: absolute;
    right: 30px; top: 66px;
    display: flex; align-items: center; gap: 14px;
  }
  .brand-dot {
    width: 40px; height: 40px; border-radius: 50%;
    background: var(--pink);
  }
  .brand-name {
    font-size: 38px; font-weight: 500;
    color: var(--ink);
    letter-spacing: 0.5px;
  }
  .address {
    position: absolute;
    right: 32px; top: 226px;
    text-align: right;
    font-size: 20px; line-height: 27px;
    color: var(--ink);
  }
</style>
</head>
<body>
  <section class="signature" aria-label="Lumora2020 e-mail signature">
    <div class="portrait-ring">
      <div class="portrait" role="img" aria-label="Portrait photo of Daniel Harper"></div>
    </div>

    <div class="divider"></div>

    <h1 class="name">Daniel Harper</h1>
    <p class="role">Founder &amp; CEO</p>

    <ul class="contacts">
      <li>
        <svg viewBox="0 0 16 16" aria-hidden="true"><path fill="#1bb1b5" d="M2 6c0-2 2.5-3.5 6-3.5S14 4 14 6v1h-3V5.8C10 5.4 9 5.3 8 5.3s-2 .1-3 .5V7H2zM4 8h8l2 5H2z"/></svg>
        000-3867-4102
      </li>
      <li>
        <svg viewBox="0 0 16 16" aria-hidden="true"><rect x="1" y="3" width="14" height="10" rx="1" fill="#f58220"/><path d="M1.5 3.8 8 9l6.5-5.2" fill="none" stroke="#fff" stroke-width="1.4"/></svg>
        info@lumorafest.com
      </li>
      <li>
        <svg viewBox="0 0 16 16" aria-hidden="true"><circle cx="8" cy="8" r="7" fill="#e8265e"/><path d="M4 5.5c1.5-.5 2.5.5 2 1.8s1 1.7 1.5 2.7-.5 2.5-1 3M10 3c-.5 1.5.5 2 1.5 2.3s1.5 1.5 1 2.7" fill="none" stroke="#fff" stroke-width="1.3"/></svg>
        <span>www.<span class="accent">lumorafest</span>.com</span>
      </li>
    </ul>

    <div class="socials" aria-label="Social profiles">
      <span class="s1"></span>
      <span class="s2"></span>
      <span class="s3"></span>
      <span class="s4"></span>
    </div>

    <div class="brand">
      <span class="brand-dot"></span>
      <span class="brand-name">Lumora2020</span>
    </div>

    <address class="address" style="font-style:normal">
      2870 HARBOR VIEW RD #214<br>
      Cedar Bay Heights
    </address>
  </section>
</body>
</html>
```